Pellham Ridge Nectar Company, local Honey producer needs product Lable to encourage sales

We are a small business (Pellham Ridge Nectar Company) located in a small Texas town that harvests honey from our beehives yearly. Our honey would be considered "raw wildflower honey" and our goal is to sell it locally (farmers markets) and to surrounding areas.

We are currently packaging in plastic classic honey bottles with white flip caps. Sizes are 8oz and 16oz bottles (see pictures for actual size). Larger orders will be filled in one quart mason jars.

Design Ideas:
-vintage style design with bee or several bees in background
- incorporate company name "Pellham Ridge Nectar Company"
- needs small description "Raw Honey", and "Harvested in Bellville, Texas"

Target Market(s)

Farmers markets, health conscience people looking for unprocessed food options

Industry/Entity Type

Small Business

Requirements
Nice to have
• Vintage feel
Should not have
• No cartoonish characters

```html
<!DOCTYPE html>
<html lang="en">
<head>
<meta charset="utf-8">
<title>Raw Honey Label – Pellham Ridge Nectar Company</title>
<link rel="stylesheet" href="https://fonts.googleapis.com/css2?family=Arvo:wght@700&family=Montserrat:wght@600;700&display=swap">
<style>
  :root {
    --ink: #161210;
    --honey: #f59b1f;
    --paper: #ffffff;
    --shadow: rgba(0, 0, 0, 0.28);
  }
  html, body {
    margin: 0;
    padding: 0;
    width: 1200px;
    height: 800px;
    overflow: hidden;
    background: var(--paper);
  }
  .canvas {
    position: relative;
    width: 1200px;
    height: 800px;
    background: var(--paper);
  }
  .label {
    position: absolute;
    left: 0;
    top: 0;
    width: 1200px;
    height: 800px;
  }
  .label__body { filter: drop-shadow(0 4px 10px var(--shadow)); }
  .company-arc {
    font-family: "Montserrat", sans-serif;
    font-weight: 600;
    font-size: 13.5px;
    letter-spacing: 3.6px;
    fill: var(--ink);
  }
  .title-raw, .title-honey {
    font-family: "Arvo", serif;
    font-weight: 700;
    fill: var(--ink);
    text-anchor: middle;
  }
  .title-raw { font-size: 50px; letter-spacing: 1px; }
  .title-honey { font-size: 72px; letter-spacing: 1px; }
  .origin-small, .origin-town, .origin-country {
    font-family: "Montserrat", sans-serif;
    font-weight: 700;
    fill: var(--ink);
    text-anchor: middle;
  }
  .origin-small { font-size: 12.5px; letter-spacing: 1px; }
  .origin-in { font-size: 7px; font-weight: 600; }
  .origin-town { font-size: 20px; letter-spacing: 1px; }
  .origin-country { font-size: 8px; letter-spacing: 0.5px; }
  .banner-state {
    font-family: "Montserrat", sans-serif;
    font-weight: 600;
    font-size: 13px;
    letter-spacing: 12px;
    fill: var(--honey);
  }
  .ink { fill: var(--ink); }
  .rule { stroke: var(--ink); stroke-linecap: round; }
</style>
</head>
<body>
<div class="canvas">
  <svg class="label" viewBox="0 0 1200 800" xmlns="http://www.w3.org/2000/svg">
    <defs>
      <path id="company-path" d="M466,316 A134,134 0 0 1 734,316"/>
      <path id="banner-path" d="M508,583 Q600,620 692,583"/>
    </defs>

    <!-- badge body -->
    <g class="label__body">
      <rect x="428" y="138" width="344" height="524" rx="172" ry="172" fill="var(--ink)"/>
      <rect x="438" y="148" width="324" height="504" rx="162" ry="162" fill="var(--honey)"/>
    </g>
    <rect x="443" y="153" width="314" height="494" rx="157" ry="157" fill="none" stroke="var(--ink)" stroke-width="2"/>

    <!-- company name on arc -->
    <text class="company-arc">
      <textPath href="#company-path" startOffset="50%" text-anchor="middle">PELLHAM RIDGE NECTAR COMPANY</textPath>
    </text>
    <g class="arc-ticks ink">
      <rect x="468" y="315" width="1.6" height="9"/>
      <rect x="471" y="315" width="1.6" height="9"/>
      <rect x="474" y="315" width="1.6" height="9"/>
      <rect x="724.4" y="315" width="1.6" height="9"/>
      <rect x="727.4" y="315" width="1.6" height="9"/>
      <rect x="730.4" y="315" width="1.6" height="9"/>
    </g>

    <!-- honeycomb emblem area -->
    <rect class="emblem-large" x="562" y="204" width="76" height="74" rx="8" fill="var(--ink)" role="img" aria-label="Distressed honeycomb cluster of three hexagon cells"/>

    <!-- title -->
    <line class="rule" x1="535" y1="297" x2="663" y2="297" stroke-width="4"/>
    <text class="title-raw" x="600" y="360">RAW</text>
    <text class="title-honey" x="600" y="427">HONEY</text>
    <line class="rule" x1="535" y1="454" x2="663" y2="454" stroke-width="4"/>

    <!-- small honeycomb -->
    <rect class="emblem-small" x="582" y="475" width="34" height="32" rx="4" fill="var(--ink)" role="img" aria-label="Small honeycomb cluster of three hexagon cells"/>

    <!-- origin -->
    <text class="origin-small" x="600" y="532">HARVESTED</text>
    <text class="origin-small origin-in" x="600" y="541">IN</text>
    <text class="origin-town" x="600" y="559">BELLVILLE</text>
    <line class="rule" x1="567" y1="571" x2="633" y2="571" stroke-width="3"/>

    <!-- banner -->
    <g class="banner ink">
      <path d="M505,570 L483,566 L494,581 L487,599 L503,592 Z"/>
      <path d="M695,570 L717,566 L706,581 L713,599 L697,592 Z"/>
      <path d="M505,570 Q600,606 695,570 L699,592 Q600,630 501,592 Z"/>
    </g>
    <circle cx="512" cy="584" r="1.3" fill="var(--honey)"/>
    <circle cx="688" cy="584" r="1.3" fill="var(--honey)"/>
    <text class="banner-state">
      <textPath href="#banner-path" startOffset="52%" text-anchor="middle">TEXAS</textPath>
    </text>

    <text class="origin-country" x="600" y="630">USA</text>
  </svg>
</div>
</body>
</html>
```